Boutique sales recruiting firm needs dual purpose business card

We need a business card designed for a sales recruiting company called Brisk Otter Recruiting. We help both sales reps looking for work as well as companies looking for talent. What makes us unique is that 'we like to hunt', not literally but hunt for great companies and greats recruits. We are looking for a business card that on one side targets sales reps looking for work and on the other side companies looking for sales reps that incorporates the feel of a "Brisk Otter" as well as having dual personalities.

```html
<!DOCTYPE html>
<html lang="en">
<head>
<meta charset="utf-8">
<title>Brisk Otter Recruiting – Business Card</title>
<link rel="stylesheet" href="https://fonts.googleapis.com/css2?family=Poppins:wght@400;500;600;700&display=swap">
<style>
  :root {
    --backdrop: #2b2b2b;
    --card-light: #ffffff;
    --card-dark: #000000;
    --ink: #111111;
    --ink-soft: #2a2a2a;
    --paper-text: #ffffff;
    --accent: #f39c12;
    --rule-light: #d8d8d8;
    --rule-dark: #8a8a8a;
  }
  * { margin: 0; padding: 0; box-sizing: border-box; }
  html, body {
    width: 1093px; height: 1200px; overflow: hidden;
    background: var(--backdrop);
    font-family: "Poppins", sans-serif;
  }
  .canvas { position: relative; width: 1093px; height: 1200px; }

  .card {
    position: absolute;
    border-radius: 26px;
    box-shadow: 0 4px 10px rgba(0,0,0,0.45);
  }
  .card--front { left: 265px; top: 226px; width: 577px; height: 356px; background: var(--card-light); color: var(--ink); }
  .card--back  { left: 265px; top: 621px; width: 583px; height: 359px; background: var(--card-dark); color: var(--paper-text); }

  .brand {
    position: absolute;
    display: flex; flex-direction: column; justify-content: center;
    font-weight: 700; line-height: 0.95;
  }
  .brand__name { font-size: 46px; letter-spacing: -1px; }
  .brand__mark { width: 16px; height: 16px; background: var(--accent); margin-top: 12px; }
  .card--front .brand { left: 61px; top: 97px; width: 160px; height: 163px; color: var(--ink); }
  .card--back .brand { left: 72px; top: 89px; width: 150px; height: 179px; color: var(--paper-text); }

  .divider { position: absolute; width: 1px; }
  .card--front .divider { left: 251px; top: 112px; height: 132px; background: var(--rule-light); }
  .card--back .divider { left: 255px; top: 124px; height: 120px; background: var(--rule-dark); }

  .person { position: absolute; left: 274px; top: 106px; }
  .person__name { font-size: 23px; font-weight: 600; color: var(--accent); line-height: 1.1; letter-spacing: 0.3px; }
  .person__title { font-size: 17px; font-weight: 400; color: var(--ink-soft); line-height: 1.2; }

  .address { position: absolute; left: 283px; top: 121px; font-size: 17px; line-height: 21px; }

  .contacts { position: absolute; list-style: none; font-size: 17.5px; line-height: 21.3px; }
  .card--front .contacts { left: 274px; top: 183px; }
  .card--back .contacts { left: 283px; top: 183px; }
  .contacts li { display: flex; align-items: center; gap: 5px; }
  .contacts svg { width: 16px; height: 16px; flex: none; }
</style>
</head>
<body>
<div class="canvas">

  <section class="card card--front" aria-label="Business card front">
    <div class="brand">
      <span class="brand__name">Brisk<br>Otter</span>
      <span class="brand__mark"></span>
    </div>
    <div class="divider"></div>
    <div class="person">
      <p class="person__name">DANIEL HARPER</p>
      <p class="person__title">Managing Director</p>
    </div>
    <ul class="contacts">
      <li>
        <svg viewBox="0 0 16 16"><path d="M4 1.5 6.2 4 5 5.6c.7 1.8 2.2 3.4 4 4.3L10.5 8.7 13.5 11l-1.5 2.6C7 13.3 2.5 8.5 2 3.4Z" fill="none" stroke="var(--accent)" stroke-width="1.6" stroke-linejoin="round"/><path d="M9.5 2.5a4.5 4.5 0 0 1 4 4M9.3 4.8a2.3 2.3 0 0 1 2 2" fill="none" stroke="var(--accent)" stroke-width="1.3"/></svg>
        055-310 782 416
      </li>
      <li>
        <svg viewBox="0 0 16 16"><rect x="0.5" y="3" width="15" height="10" fill="var(--accent)"/><path d="M0.5 3 8 9l7.5-6M0.5 13l5.5-5M15.5 13 10 8" fill="none" stroke="#fff" stroke-width="1"/></svg>
        hello@briskotter.com
      </li>
      <li>
        <svg viewBox="0 0 16 16"><g fill="none" stroke="var(--accent)" stroke-width="1.3"><circle cx="8" cy="8" r="6.8"/><ellipse cx="8" cy="8" rx="3" ry="6.8"/><path d="M1.2 8h13.6M2.2 4.6h11.6M2.2 11.4h11.6M8 1.2v13.6"/></g></svg>
        www.briskotter.com
      </li>
    </ul>
  </section>

  <section class="card card--back" aria-label="Business card back">
    <div class="brand">
      <span class="brand__name">Brisk<br>Otter</span>
      <span class="brand__mark"></span>
    </div>
    <div class="divider"></div>
    <p class="address">421, Address line goes here<br>45452,Country Name</p>
    <ul class="contacts">
      <li>
        <svg viewBox="0 0 16 16"><path d="M4 1.5 6.2 4 5 5.6c.7 1.8 2.2 3.4 4 4.3L10.5 8.7 13.5 11l-1.5 2.6C7 13.3 2.5 8.5 2 3.4Z" fill="none" stroke="var(--accent)" stroke-width="1.6" stroke-linejoin="round"/><path d="M9.5 2.5a4.5 4.5 0 0 1 4 4M9.3 4.8a2.3 2.3 0 0 1 2 2" fill="none" stroke="var(--accent)" stroke-width="1.3"/></svg>
        055-310 782 416
      </li>
      <li>
        <svg viewBox="0 0 16 16"><rect x="0.5" y="3" width="15" height="10" fill="var(--accent)"/><path d="M0.5 3 8 9l7.5-6M0.5 13l5.5-5M15.5 13 10 8" fill="none" stroke="#000" stroke-width="1"/></svg>
        hello@briskotter.com
      </li>
      <li>
        <svg viewBox="0 0 16 16"><g fill="none" stroke="var(--accent)" stroke-width="1.3"><circle cx="8" cy="8" r="6.8"/><ellipse cx="8" cy="8" rx="3" ry="6.8"/><path d="M1.2 8h13.6M2.2 4.6h11.6M2.2 11.4h11.6M8 1.2v13.6"/></g></svg>
        www.briskotter.com
      </li>
    </ul>
  </section>

</div>
</body>
</html>
```